依頼詳細
今回作成頂くヘッダーを下記のサイトの最上部に設置させて頂きます。

http://k-plomev.net/027/sample-4/

読者集めのためのLPとなりまして
ヘッダーのデザイン一つで、読み進めて頂けるかどうかという
重要な要素となっております。

ターゲットは主に男性です。

暗めのデザインではなく、
清潔感あるデザインを望んでおります。

【フォント】
フォントは、
・源の角ゴシック(オープンソース無料でインストール頂けます)
・AXIS

などのような見た目の洗練されたフォントと

・明朝

のような2種のフォントを混ぜて作成してください。

【サイズ】
元サイトの横幅が900pixですが、
ヘッダーだけは、幅1200pixで作成して頂きたいと思っております。

【参考デザイン】
今回のヘッダーデザインの雰囲気を感じて頂くために
こちらも別途資料を添付させて頂きます。

採用の可能性が高い作品に関しましては、
必要に応じ、修正依頼をさせて頂きまして
再度、投稿をお願いすることもあるかと存じます。

皆様からの素晴らしい作品をお待ち致しております。
何卒宜しくお願いいたします。

尚、弊社では今回のLP作成以外にも
デザインの案件を持っております。

今後もお付き合いいただけるデザイナー様は大変嬉しく思います。
記載項目
別途資料を添付させて頂きました。
サイズ
• 幅1200× 高さはコピーに合わせて
希望イメージ
シンプル 複雑
単色 カラフル
暗い 明るい
日常 高級
遊び心 厳粛
未来的 伝統的
女性的 男性的
希望する色
青系、黄・オレンジ系、重ための色以外で、デザイナー様にお任せします。
納品ファイル
• 高解像度JPG (.jpg)
補足説明
ヘッダーのコピーを添付させて頂きます。
コピーは決まっていますが、この中に画像を入れて頂いたり、
少しコピーの並びや文章を変えてデザイン的に作成頂いても大歓迎です。
■ 選んだ理由

イメージに即した素敵な作品でした。

■ 提案者全員のお礼・コメント

この度は誠に有り難うございました。

```html
<!DOCTYPE html>
<html lang="ja">
<head>
<meta charset="utf-8">
<title>究極のハイブリッド輸入ビジネス</title>
<link href="https://fonts.googleapis.com/css2?family=Noto+Sans+JP:wght@400;700;900&family=Noto+Serif+JP:wght@700;900&display=swap" rel="stylesheet">
<style>
:root{
  --red:#d4121b;
  --gold-1:#fff6c8;
  --gold-2:#f2cf5a;
  --gold-3:#c8951c;
  --ink:#1a1a1a;
  --gray:#6b6b6b;
  --blue:#1763b8;
  --sky-1:#e9f3fb;
  --sky-2:#9ccbea;
  --white:#ffffff;
}
*{margin:0;padding:0;box-sizing:border-box}
html,body{width:849px;height:1200px;overflow:hidden;background:var(--white)}
body{font-family:"Noto Sans JP",sans-serif;color:var(--ink);position:relative}
.campaign-banner{
  position:absolute;left:0;top:0;width:849px;height:107px;
  background:linear-gradient(180deg,var(--gold-1) 0%,var(--gold-2) 55%,var(--gold-3) 100%);
  display:flex;align-items:center;justify-content:center;white-space:nowrap;
  font-weight:900;font-size:40px;color:var(--red);
  text-shadow:0 2px 0 #fff;
}
.hero-visual{
  position:absolute;left:0;top:290px;width:849px;height:560px;
  background:radial-gradient(ellipse at 45% 65%,#2f7fc9 0%,var(--sky-2) 38%,var(--sky-1) 70%,var(--white) 100%);
}
.hero-fade{
  position:absolute;left:0;top:680px;width:849px;height:200px;
  background:linear-gradient(90deg,rgba(255,255,255,0) 0%,rgba(255,255,255,.85) 30%,rgba(255,255,255,.95) 100%);
}
.teaser{
  position:absolute;left:170px;top:127px;width:510px;height:162px;
  border:2px solid #bdbdbd;background:var(--white);
  display:flex;flex-direction:column;align-items:center;justify-content:center;
  font-weight:700;font-size:26px;line-height:1.55;white-space:nowrap;
}
.teaser .em{color:var(--red);font-size:30px;font-weight:900}
.headline{
  position:absolute;left:0;top:317px;width:849px;height:96px;
  background:rgba(255,255,255,.88);
  display:flex;align-items:center;justify-content:center;white-space:nowrap;
  font-weight:900;font-size:42px;
}
.features{position:absolute;right:22px;top:690px;width:780px;list-style:none}
.features li{
  display:flex;align-items:baseline;justify-content:flex-end;white-space:nowrap;
  height:68px;padding-top:14px;border-bottom:2px solid rgba(120,170,215,.6);margin-bottom:6px;
}
.features .lead{font-size:21px;color:var(--gray);font-weight:400}
.features .point{font-family:"Noto Serif JP",serif;font-weight:900;font-size:30px;color:var(--ink)}
.no-matter{
  position:absolute;left:0;top:925px;width:849px;text-align:center;white-space:nowrap;
  font-weight:900;font-size:33px;color:var(--blue);line-height:50px;
}
.no-matter .small{font-size:26px}
.no-matter .accent{color:var(--red)}
.promise{position:absolute;left:14px;top:992px;width:821px;height:180px}
.promise-text{
  position:absolute;left:0;top:0;width:821px;height:162px;
  display:flex;flex-direction:column;align-items:center;justify-content:center;white-space:nowrap;
  font-family:"Noto Serif JP",serif;font-weight:900;color:var(--white);
  font-size:40px;line-height:1.4;
}
</style>
</head>
<body>
  <div class="campaign-banner">期間限定！緊急特別キャンペーン！！</div>

  <div class="hero-visual" role="img" aria-label="地球儀の周りに多くの人物写真が浮かぶ青いグローバルイメージ"></div>
  <div class="hero-fade"></div>

  <div class="teaser">
    <span>1日1時間の作業で</span>
    <span>月収<span class="em">350万円</span> 年商<span class="em">1億5000万円</span>を稼ぐ</span>
    <span>秘密を知りたいですか?</span>
  </div>

  <h1 class="headline">究極のハイブリッド輸入ビジネス</h1>

  <ul class="features">
    <li><span class="lead">アカウント停止に怯えない</span><span class="point">『多販路リスクヘッジ物販』</span></li>
    <li><span class="lead">フルオートで収益が上がり続ける</span><span class="point">『真の仕組み構築』</span></li>
    <li><span class="lead">合理的ノウハウに保証された</span><span class="point">『驚愕の時間短縮ノウハウ』</span></li>
  </ul>

  <p class="no-matter">実績・年齢・性別・職業・居住地<span class="small">なんて</span><span class="accent">関係なし！</span></p>

  <div class="promise">
    <svg width="821" height="180" viewBox="0 0 821 180" aria-hidden="true">
      <defs>
        <linearGradient id="promiseFill" x1="0" y1="0" x2="0" y2="1">
          <stop offset="0" stop-color="#2a7fd0"/>
          <stop offset="1" stop-color="#0c4a93"/>
        </linearGradient>
      </defs>
      <path d="M3 3 H818 V160 H434 L410 178 L386 160 H3 Z" fill="url(#promiseFill)" stroke="#e0b23a" stroke-width="4"/>
    </svg>
    <div class="promise-text">
      <span>ハイブリッド輸入ビジネスでの稼ぎ方の</span>
      <span>すべてを私が伝授します！</span>
    </div>
  </div>
</body>
</html>
```